Website redesign for Root and Renew

We would like to update the design of our current website to a more concise, conversion optimized design.
The goal of our website is to get our message across as concisely as possible plus encourage people to contact us for more information or to book a consultation.
We need a redesign of the home page and 1 internal page - just for design/layout purposes/format purposes.

Target Market(s)

Males 20-45 years old who are concerned about hair loss and who want to regrow their own hair.

Industry/Entity Type

Health And Wellness

Number of Pages Required

2 page

Font styles to use
Sans Serif

Colors
00a990
33a6d7
ffffff
9d9d9d

Requirements
Must have
• We want the home page to be very concise and to the point in getting the message across. We want to get across the following 6 key messages:
• 1. Dr Brambury story – why he created this solution
• 2. Hair loss is caused by a chemical imbalance
• 3. Root and renew conducts genetic and DNA analysis, then rebalances body chemistry, thus reversing the hair loss process and enabling your own hair to regrow naturally
• 4. Money back guaranteed results
• 5. Purely The Core ingredients – no harsh preservatives or chemicals are included
• 6. All ingredients are FDA approved and safe – no side effects
• We also need a strong call to action. We want people to call or email us to find out more information or to schedule a consultation.
• Here is our current website which is not performing as we would hope: http://www.rootandrenewhq.com/
• Here is our press release for further information: https://www.pressflarex.com/news/finally-we-now-have-a-cure-for-male-pattern-baldness-40528316
• I uploaded the logo files, but let me know if anything else is needed and I can add it.

```html
<!DOCTYPE html>
<html lang="en">
<head>
<meta charset="utf-8">
<title>Root and Renew — Regrow Your Own Hair Naturally</title>
<link href="https://fonts.googleapis.com/css2?family=Alegreya+Sans:ital,wght@0,400;0,500;0,700;0,800;1,400;1,500&display=swap" rel="stylesheet">
<style>
:root{
  --green:#00a990;
  --blue:#33a6d7;
  --band:#4fbfe0;
  --ink:#1b1b1b;
  --text:#8a8a8a;
  --grey:#9d9d9d;
  --rule:#e6e6e6;
  --soft:#f4f4f4;
  --footer:#1e1e1e;
  --white:#ffffff;
}
*{box-sizing:border-box;margin:0;padding:0}
html,body{width:1200px;height:3982px;overflow:hidden}
body{position:relative;background:var(--white);font-family:"Alegreya Sans",Arial,sans-serif;color:var(--ink)}
.abs{position:absolute}
.center{left:0;width:1200px;text-align:center}
h2.section-title{font-size:42px;font-weight:700;line-height:1.22;color:var(--ink)}
.lead{color:var(--green);font-size:24px}
.small{font-size:15px;color:var(--text);line-height:1.55}
.btn{display:inline-block;border-radius:22px;font-size:15px;font-weight:700;text-align:center;line-height:42px;height:42px}
.btn-green{background:var(--green);color:var(--white)}
.btn-dark{background:#121212;color:var(--white)}
.rule{height:1px;background:var(--rule);left:85px;width:1030px}

/* header */
.site-header{top:0;left:0;width:1200px;height:101px;background:var(--white)}
.brand{left:62px;top:24px;display:flex;align-items:center;gap:12px}
.brand-mark{width:30px;height:30px;border-radius:50%;background:var(--green)}
.brand-name{font-size:24px;font-weight:500;color:#333;line-height:1}
.brand-by{font-size:15px;font-weight:500;color:#333;line-height:1;margin-top:4px}
.nav-item{top:38px;font-size:15px;color:#333}
.nav-item.active{color:var(--green)}
.caret{font-size:10px;margin-left:4px}
.search{left:1102px;top:40px}

/* hero */
.hero{top:101px;left:0;width:1200px;height:419px;background:linear-gradient(90deg,#8a8a8a 0%,#6e6e6e 45%,#9b9b9b 100%)}
.hero-title{top:180px;font-size:42px;font-weight:700;color:var(--white)}
.hero-sub{top:250px;font-size:24px;color:var(--white)}
.hero-note{top:306px;font-size:15px;color:var(--white);line-height:1.5}
.hero-btn{top:385px;left:497px;width:207px}
.dots{top:480px;left:564px;display:flex;gap:16px}
.dots i{width:10px;height:10px;border-radius:50%;background:#3a3a3a;display:block}
.dots i.on{background:var(--green)}

/* services */
.service-img{top:1033px;width:237px;height:236px}
.service-label{top:1302px;width:237px;text-align:center;color:var(--green);font-size:22px;line-height:1.25}

/* consult */
.consult{top:1516px;left:0;width:1200px;height:507px;background:var(--soft)}
.consult-photo{top:1516px;left:797px;width:403px;height:507px;background:linear-gradient(90deg,#eeeeee,#d9d1c9 45%,#c9bdb2)}

/* why */
.why-img{top:2172px;width:326px;height:236px}
.why-label{top:2436px;width:326px;text-align:center;color:var(--green);font-size:22px}
.why-text{top:2476px;width:326px;text-align:center}

/* testimonials */
.avatar{top:2801px;width:100px;height:100px;border-radius:50%;background:linear-gradient(#c9c9c9,#8f8f8f);border:3px solid #eee}
.quote-mark{top:2918px;width:260px;text-align:center;color:var(--green);font-size:44px;font-weight:800;line-height:1}
.quote{top:2952px;width:260px;text-align:center;font-size:15px;color:var(--text);line-height:1.45}
.quote-name{top:3088px;width:260px;text-align:center;font-size:16px;font-weight:700;color:var(--ink)}

/* cta */
.cta{top:3191px;left:0;width:1200px;height:449px;background:var(--band)}

/* footer */
.footer{top:3640px;left:0;width:1200px;height:342px;background:var(--footer)}
.f-head{top:3716px;font-size:17px;font-weight:700;color:var(--white)}
.f-text{font-size:15px;color:var(--grey);line-height:1.5}
.f-italic{font-style:italic}
.f-icon{width:18px;height:18px}
.social{top:3951px;left:930px;display:flex;gap:28px}
.social i{width:12px;height:12px;border-radius:50%;background:#8a8a8a;display:block}
</style>
</head>
<body>

<header class="abs site-header">
  <div class="abs brand">
    <div class="brand-mark"></div>
    <div>
      <div class="brand-name">Root and Renew</div>
      <div class="brand-by">by Dr Brambury</div>
    </div>
  </div>
  <span class="abs nav-item active" style="left:504px">Home<span class="caret">▾</span></span>
  <span class="abs nav-item" style="left:600px">About us</span>
  <span class="abs nav-item" style="left:711px">Services<span class="caret">▾</span></span>
  <span class="abs nav-item" style="left:820px">News<span class="caret">▾</span></span>
  <span class="abs nav-item" style="left:910px">Contacts</span>
  <span class="abs nav-item" style="left:1022px">Pages<span class="caret">▾</span></span>
  <svg class="abs search" width="16" height="16" viewBox="0 0 16 16"><circle cx="6.5" cy="6.5" r="4.8" fill="none" stroke="#333" stroke-width="2"/><line x1="10" y1="10" x2="14.5" y2="14.5" stroke="#333" stroke-width="2.2" stroke-linecap="round"/></svg>
</header>

<section class="abs hero" role="img" aria-label="Photo of a man touching his hairline, grey toned"></section>
<h1 class="abs center hero-title">Regrow your own hair, naturally!</h1>
<p class="abs center hero-sub">Guaranteed results, or your money back!</p>
<p class="abs center hero-note">Our genetic and DNA analysis lets us rebalance your body chemistry,<br>reversing hair loss so your own hair can regrow naturally!</p>
<span class="abs btn btn-green hero-btn">Book a Consultation</span>
<div class="abs dots"><i></i><i></i><i class="on"></i></div>

<h2 class="abs center section-title" style="top:594px">It's not about hair loss, it's about hair recovery...</h2>
<p class="abs center lead" style="top:660px">Hair loss is caused by a chemical imbalance in your body!</p>
<p class="abs center small" style="top:718px">Dr Brambury created this solution after seeing patients try treatments that only hid the problem, so he set out to fix<br>the real cause and let your own hair grow back naturally!</p>
<div class="abs rule" style="top:836px"></div>

<h2 class="abs center section-title" style="top:904px">See how we reverse hair loss and<br>help your own hair regrow:</h2>
<div class="abs service-img" style="left:85px;background:linear-gradient(#d8b9a6,#b98e77)" role="img" aria-label="Shaved scalp with a marked hairline"></div>
<div class="abs service-img" style="left:348px;background:linear-gradient(#ececec,#7a5a48)" role="img" aria-label="Back of a head with a thinning crown"></div>
<div class="abs service-img" style="left:613px;background:linear-gradient(#f2f2f2,#c9d0d6)" role="img" aria-label="Gloved hands treating a scalp"></div>
<div class="abs service-img" style="left:878px;background:linear-gradient(#f5eee8,#b2836a)" role="img" aria-label="Close-up of a scalp during treatment"></div>
<p class="abs service-label" style="left:85px">DNA Hair Analysis</p>
<p class="abs service-label" style="left:348px">Genetic Profile<br>Testing</p>
<p class="abs service-label" style="left:613px">Body Chemistry<br>Rebalancing</p>
<p class="abs service-label" style="left:878px">Natural Hair<br>Regrowth</p>
<span class="abs btn btn-green" style="top:1394px;left:520px;width:160px">See all Services</span>

<section class="abs consult"></section>
<div class="abs consult-photo" role="img" aria-label="Smiling man in a shirt and tie"></div>
<h2 class="abs section-title" style="top:1588px;left:85px;text-align:left">Looking for consultation or hair<br>care assistance?</h2>
<p class="abs lead" style="top:1724px;left:85px;font-size:22px;line-height:1.6;font-style:italic">Call or email us today to find out more or to book a<br>consultation with Dr Brambury and our team, who will<br>find the cause and help your own hair regrow naturally.</p>
<span class="abs btn btn-dark" style="top:1891px;left:85px;width:212px">Book a Consultation</span>

<h2 class="abs center section-title" style="top:2094px">Why our Hair Recovery Clinic is the best?</h2>
<div class="abs why-img" style="left:85px;background:linear-gradient(#e9e9e9,#4a3a30)" role="img" aria-label="Side view of a man's thick dark hair"></div>
<div class="abs why-img" style="left:438px;background:linear-gradient(#f4f4f4,#b9c7d2)" role="img" aria-label="Clinic staff in uniforms"></div>
<div class="abs why-img" style="left:789px;background:linear-gradient(#eef2f5,#c3ccd3)" role="img" aria-label="Natural ingredients for hair treatment"></div>
<p class="abs why-label" style="left:85px">Money Back Guarantee</p>
<p class="abs why-label" style="left:438px">Purely The Core Ingredients</p>
<p class="abs why-label" style="left:789px">FDA Approved &amp; Safe</p>
<p class="abs small why-text" style="left:85px">Your results are guaranteed: if your own hair<br>does not regrow, you get your money back!</p>
<p class="abs small why-text" style="left:438px">We use only core ingredients, with no<br>harsh preservatives or chemicals added<br>to any of our hair treatments!</p>
<p class="abs small why-text" style="left:789px">All of our ingredients are FDA approved<br>and safe to use, so there are no side<br>effects to worry about at any point of<br>your treatment...</p>
<div class="abs rule" style="top:2642px"></div>

<h2 class="abs center section-title" style="top:2714px">See what our Happy Patients say</h2>
<div class="abs avatar" style="left:197px" role="img" aria-label="Patient portrait"></div>
<div class="abs avatar" style="left:550px" role="img" aria-label="Patient portrait"></div>
<div class="abs avatar" style="left:901px" role="img" aria-label="Patient portrait"></div>
<div class="abs quote-mark" style="left:117px">“</div>
<div class="abs quote-mark" style="left:470px">“</div>
<div class="abs quote-mark" style="left:821px">“</div>
<p class="abs quote" style="left:117px">I began to lose my hair on the forehead at 35 and tried every product out there. The DNA analysis found the real cause, and now my own hair is growing back!</p>
<p class="abs quote" style="left:470px">I was worried about harsh chemicals and side effects, but every ingredient is FDA approved and safe. Dr Brambury explained it all, and I've never felt happier!</p>
<p class="abs quote" style="left:821px">I started balding in my late 20s. Rebalancing my body chemistry stopped the loss, and the money back guarantee made it an easy choice. Thanks!</p>
<p class="abs quote-name" style="left:117px">Daniel Carver</p>
<p class="abs quote-name" style="left:470px">Jonah Mercer</p>
<p class="abs quote-name" style="left:821px">Benedict Darrow</p>

<section class="abs cta"></section>
<h2 class="abs center section-title" style="top:3296px;color:var(--white)">Do you suffer from balding or want to prevent it timely?</h2>
<p class="abs center" style="top:3384px;color:var(--white);font-size:23px;line-height:1.7;font-style:italic">Call 555-010-4417 or email info@rootandrenewhq.com to find out more<br>or to schedule your consultation today!</p>
<span class="abs btn btn-dark" style="top:3494px;left:495px;width:210px">Book a Consultation</span>

<footer class="abs footer"></footer>
<h3 class="abs f-head" style="left:82px">About us</h3>
<h3 class="abs f-head" style="left:435px">Contact info</h3>
<h3 class="abs f-head" style="left:789px">Opening hours</h3>
<p class="abs f-text" style="top:3755px;left:82px;width:300px">Root and Renew by Dr Brambury rebalances your body chemistry so your own hair can regrow naturally.</p>

<svg class="abs f-icon" style="top:3762px;left:438px" viewBox="0 0 18 18"><circle cx="9" cy="9" r="9" fill="#3a3a3a"/><path d="M6 5l2 0 1 3-1.3 1a6 6 0 0 0 2.3 2.3l1-1.3 3 1 0 2c-4 .5-8.5-4-8-8z" fill="#bbb"/></svg>
<p class="abs f-text f-italic" style="top:3758px;left:478px">555-010-4417, 555-010-4418</p>
<svg class="abs f-icon" style="top:3810px;left:438px" viewBox="0 0 18 18"><circle cx="9" cy="9" r="9" fill="#3a3a3a"/><rect x="4.5" y="6" width="9" height="6.5" fill="none" stroke="#bbb" stroke-width="1.3"/><path d="M4.5 6l4.5 3.5 4.5-3.5" fill="none" stroke="#bbb" stroke-width="1.3"/></svg>
<p class="abs f-text f-italic" style="top:3806px;left:478px">info@rootandrenewhq.com</p>
<svg class="abs f-icon" style="top:3858px;left:438px" viewBox="0 0 18 18"><circle cx="9" cy="9" r="9" fill="#3a3a3a"/><path d="M9 3.5a3.5 3.5 0 0 0-3.5 3.5c0 2.6 3.5 7 3.5 7s3.5-4.4 3.5-7A3.5 3.5 0 0 0 9 3.5z" fill="#bbb"/><circle cx="9" cy="7" r="1.3" fill="#3a3a3a"/></svg>
<p class="abs f-text f-italic" style="top:3854px;left:478px">48 Larch Lane Orlando, FL 3457</p>

<svg class="abs f-icon" style="top:3762px;left:792px" viewBox="0 0 18 18"><circle cx="9" cy="9" r="9" fill="#3a3a3a"/><circle cx="9" cy="9" r="5" fill="none" stroke="#bbb" stroke-width="1.3"/><path d="M9 6v3.2l2 1.3" fill="none" stroke="#bbb" stroke-width="1.3"/></svg>
<p class="abs f-text f-italic" style="top:3756px;left:832px;line-height:1.45">Monday–Friday: 9am–6pm<br>Saturday: 10am–4pm<br>Sunday: 10am–1pm</p>

<div class="abs social"><i></i><i></i><i></i><i></i><i></i></div>

</body>
</html>
```